Request for Business Card Design

Hi. My name is Marlena, I am looking for a new business card design for my company, Quillbrook Sensing Systems, LLC. I really like the design you did for Tavel Harvest and was hoping you could do something similar using our full logo and our mark. I am also open to any raised texture design using our mark. I have attached our full logo, which would need to be somewhere on the card, as well as the mark in both outline and full form, as well as our brand colors / guide. The card does not have to be white, as long as our logo and mark appear. I actually like darker colored business cards more, but am open to all options. If you are interested in working with me, please let me know. We would also take the business card design into letterhead design if you can do that.

```html
<!DOCTYPE html>
<html lang="en">
<head>
<meta charset="utf-8">
<title>Quillbrook Sensing Systems — Stationery</title>
<link href="https://fonts.googleapis.com/css2?family=Lato:wght@400;700&family=Montserrat:wght@400;600;700&family=Italianno&display=swap" rel="stylesheet">
<style>
  :root {
    --brand-blue: #0b93bb;
    --brand-dark: #3b3b3d;
    --text: #444446;
    --paper: #ffffff;
    --backdrop: #e7e4e3;
  }
  * { box-sizing: border-box; margin: 0; padding: 0; }
  html, body { width: 1200px; height: 900px; overflow: hidden; }
  body { background: var(--backdrop); position: relative; font-family: "Lato", sans-serif; color: var(--text); }

  .brand { display: flex; align-items: center; gap: 8px; }
  .brand-dot { border-radius: 50%; background: var(--brand-blue); flex: none; }
  .brand-name { font-family: "Lato", sans-serif; font-weight: 700; text-transform: uppercase; letter-spacing: 1.5px; line-height: 1.1; }

  /* Letterhead */
  .letterhead { position: absolute; left: 200px; top: 122px; width: 464px; height: 656px; background: var(--paper); box-shadow: 0 8px 24px rgba(0,0,0,.15); }
  .letterhead .brand { position: absolute; left: 36px; top: 48px; }
  .letterhead .brand-dot { width: 36px; height: 36px; }
  .letterhead .brand-name { font-size: 15px; color: var(--brand-dark); width: 170px; }
  .letterhead-contact { position: absolute; left: 314px; top: 34px; border-left: 1px solid var(--brand-blue); padding-left: 5px; font-size: 7.6px; line-height: 11px; color: #222; }
  .letterhead-contact .address { margin-bottom: 3px; }
  .contact-row { display: flex; align-items: center; gap: 5px; }
  .contact-row svg { width: 7px; height: 7px; fill: var(--brand-blue); flex: none; }
  .letter { position: absolute; left: 36px; top: 150px; width: 393px; font-size: 8.6px; line-height: 10.2px; }
  .letter-date { margin-bottom: 11px; }
  .letter-recipient { margin-bottom: 10px; }
  .letter-greeting { font-size: 11px; font-weight: 700; margin: 10px 0 11px; color: #333; }
  .letter p { text-align: justify; margin-bottom: 10px; }
  .letter-closing { margin-top: 26px; }
  .letter-signature { font-family: "Italianno", cursive; font-size: 28px; color: #333; margin-top: 12px; }
  .letterhead-footer { position: absolute; left: 0; bottom: 0; width: 464px; height: 30px; display: block; }

  /* Business card front */
  .card { position: absolute; width: 326px; height: 188px; box-shadow: 0 8px 20px rgba(0,0,0,.15); }
  .card-front { left: 700px; top: 250px; background: var(--paper); font-family: "Montserrat", sans-serif; }
  .card-holder { position: absolute; left: 14px; top: 22px; }
  .card-holder-name { font-size: 10px; font-weight: 700; color: var(--brand-dark); text-transform: uppercase; }
  .card-holder-name .first { color: var(--brand-blue); }
  .card-holder-role { font-size: 8.4px; color: #222; margin-top: 2px; }
  .card-front .brand { position: absolute; right: 14px; top: 18px; gap: 6px; }
  .card-front .brand-dot { width: 26px; height: 26px; }
  .card-front .brand-name { font-size: 10.5px; color: var(--brand-dark); width: 118px; }
  .card-contact { position: absolute; left: 14px; top: 119px; font-size: 8.2px; line-height: 13px; color: #222; }
  .card-contact .contact-row svg { width: 8px; height: 8px; }
  .card-address { position: absolute; right: 14px; top: 132px; font-size: 8.2px; line-height: 11.5px; text-align: right; color: #222; }
  .card-footer { position: absolute; left: 0; bottom: 0; width: 326px; height: 22px; display: block; }

  /* Business card back */
  .card-back { left: 700px; top: 470px; background: var(--brand-blue); display: flex; align-items: center; justify-content: center; }
  .card-back .brand { gap: 10px; }
  .card-back .brand-dot { width: 44px; height: 44px; background: var(--paper); }
  .card-back .brand-name { font-size: 17px; color: var(--paper); width: 190px; }
</style>
</head>
<body>

<section class="letterhead" aria-label="Letterhead">
  <div class="brand">
    <span class="brand-dot"></span>
    <span class="brand-name">Quillbrook Sensing Systems</span>
  </div>

  <div class="letterhead-contact">
    <div class="address">42-06 Fenwick Rd 8<br>Ashford, NY 11907</div>
    <div class="contact-row"><svg viewBox="0 0 10 10"><path d="M2 0.5l2 2-1 1.3c.6 1.3 1.6 2.3 2.9 2.9L7.2 5.6l2 2-1.2 1.6C4.5 9 1 5.5.6 1.7z"/></svg>555-0142-7781</div>
    <div class="contact-row"><svg viewBox="0 0 10 10"><path d="M0 2h10v6H0z M0 2l5 3.5L10 2" stroke="#fff" stroke-width=".8"/></svg>hello@quillbrook-sensing.com</div>
    <div class="contact-row"><svg viewBox="0 0 10 10"><circle cx="5" cy="5" r="4.8"/></svg>www.quillbrook-sensing.com</div>
  </div>

  <div class="letter">
    <div class="letter-date">Feb-03-2022</div>
    <div class="letter-recipient">Mr, Alden Price<br>President</div>
    <div class="letter-recipient">Harrow Works<br>48 Linden Row, Suite# 6<br>Brookfield, State, 440219</div>
    <div class="letter-greeting">Dear Mr, Alden</div>
    <p>Lorem ipsum dolor sit amet, consectetur adipisicing elit, sed do eiusmod tempor incididunt ut labore et dolore magna aliqua. Ut enim ad minim veniam, quis nostrud exercitation ullamco laboris nisi ut aliquip ex ea commodo consequat. Duis aute irure dolor in reprehenderit in voluptate velit esse cillum dolore eu fugiat nulla pariatur.</p>
    <p>Lorem ipsum dolor sit amet, consectetur adipisicing elit, sed do eiusmod tempor incididunt ut labore et dolore magna aliqua. Ut enim ad minim veniam, quis nostrud exercitation ullamco laboris nisi ut aliquip ex ea commodo consequat. Duis aute irure dolor in reprehenderit in voluptate velit esse cillum dolore eu fugiat nulla pariatur.</p>
    <p>Lorem ipsum dolor sit amet, consectetur adipisicing elit, sed do eiusmod tempor incididunt ut labore et dolore magna aliqua. Ut enim ad minim veniam, quis nostrud exercitation ullamco laboris nisi ut aliquip ex ea commodo consequat.</p>
    <p>Excepteur sint occaecat cupidatat non proident, sunt in culpa qui officia deserunt mollit anim id est laborum. re et dolore magnam aliquam quaerat voluptatem.</p>
    <div class="letter-closing">Regards</div>
    <div class="letter-signature">Owen Hartley</div>
  </div>

  <svg class="letterhead-footer" viewBox="0 0 464 30" aria-hidden="true">
    <rect x="0" y="1" width="98" height="6" fill="var(--brand-dark)"/>
    <rect x="102" y="1" width="80" height="6" fill="var(--brand-blue)"/>
    <polygon points="185,1 302,1 296,7 185,7" fill="var(--brand-dark)"/>
    <polygon points="311,0 464,0 464,30 0,30 0,13 298,13" fill="var(--brand-blue)"/>
  </svg>
</section>

<section class="card card-front" aria-label="Business card front">
  <div class="card-holder">
    <div class="card-holder-name"><span class="first">Tessa</span> Varnell</div>
    <div class="card-holder-role">Owner</div>
  </div>
  <div class="brand">
    <span class="brand-dot"></span>
    <span class="brand-name">Quillbrook Sensing Systems</span>
  </div>
  <div class="card-contact">
    <div class="contact-row"><svg viewBox="0 0 10 10"><path d="M1 3.5C1 2 3 1.2 5 1.2S9 2 9 3.5V4.5H7V3.5H3v1H1z M2 5h6l1 4H1z" fill="var(--brand-blue)"/></svg>555.204.6613</div>
    <div class="contact-row"><svg viewBox="0 0 10 10"><path d="M0 2h10v6H0z M0 2l5 3.5L10 2" stroke="#fff" stroke-width=".8"/></svg>info@quillbrooksensing.com</div>
    <div class="contact-row"><svg viewBox="0 0 10 10"><circle cx="5" cy="5" r="4.8"/></svg>www.quillbrooksensing.com</div>
  </div>
  <div class="card-address">2840 Calloway Ave, Ste<br>300, Brenton, TX 750188</div>
  <svg class="card-footer" viewBox="0 0 326 22" aria-hidden="true">
    <rect x="0" y="1" width="69" height="4" fill="var(--brand-dark)"/>
    <rect x="71" y="1" width="56" height="4" fill="var(--brand-blue)"/>
    <polygon points="129,1 211,1 207,5 129,5" fill="var(--brand-dark)"/>
    <polygon points="217,0 326,0 326,22 0,22 0,10 208,10" fill="var(--brand-blue)"/>
  </svg>
</section>

<section class="card card-back" aria-label="Business card back">
  <div class="brand">
    <span class="brand-dot"></span>
    <span class="brand-name">Quillbrook Sensing Systems</span>
  </div>
</section>

</body>
</html>
```